RESTAURANT MENU

WANTING TO CHANGE MENU DESIGN AND ADD SOME PLATES AND DESSERTS

ILL POST PICTURES OF LOGO AND PLATES. DONT HAVE ANYTHING IN MIND JUST NEED SOMETHING NEW THAT WILL STAND OUT .

Industry/Entity Type

Restaurant

Requirements
Must have
• THE SIZE RIGHT NOW IS 11X17 TRIFOLD MENU.
• IF ITS TOO CROWDED WITH THE NEW PLATES I DONT MIND MAKING IT BIGGER .
• ADD ONS
• ******************************** PASTAS **************************
• CHICKEN FETTUCCINE OR PENNE PASTA - 9.25
• SHRIMP FETTUCCINE OR PENNE PAST 10.25
• ******************* WINGS ***************************************
• BONELESS OR TRADITIONAL
• 5 WINGS - 5.99
• 10 WINGS - 8.99
• 20 WINGS - 14.99
• 50 WINGS - 35.99
• mild , hot , lemon pepper , sweet chili , teriyaki , garlic Parmesan
• *****************FROM THE BAR-B-QUE*************
• BABY BACK RIBS
• half rack - 12.99
• full rack - 18.99
• BRISKET BURGER 8.25
• BARBECUE COMBO - 17.99
• half rack of ribs, brisket , and sausage
• served with potato salad and red beans.
Should not have
• ADRESS CORRECTION ****
• 418 N. MARLOWE AVE.
• ELSA TEXAS
• ************* APPETIZERS***********
• Jalapeno cheese fries ............................. 4.99
• Mozzarella cheese sticks ........................ 5.25
• Classic Nachos ( ground bee) ................. 6.99
• Nachos ( fajita or chicken fajita ).............. 7.99
• Panchos ....................................................8.99
• ( includes lettuce , and avocado )
• Shrimp Nachos ........................................8.99
• Choriqueso...............................................6.99
• Guacamole ..............................................5.99
• ***************SALADS******************
• House Salad ...........................................5.99
• Caesar Salad...........................................5.99
• Chef Salad ...............................................7.99
• Grilled or Crispy chicken Salad ................8.99
• Shrimp Salad ............................................9.99
• ***************BURGERS AND SANDWICHES ****************
• Fajita Steak Burger .............................................................8.95
• (fine cut fajita loaded with fresh sauteed mushrooms , and topped with
• mozzarella cheese, crisp lettuce , onions , tomatoes mayo & mustard)
• Mushroom Swiss Burger .....................................................8.95
• (loaded with fresh saureed mushrooms, and topped with melted Swiss cheese)
• Hawaiian Burger ..................................................................7.99
• (topped with pineapple , american cheese , crisp lettuce , tomatoes and mayo. )
• Barbecue Burger.......................................................................7.99
• (basted with our original Bbq sauce, American cheese , lettuce , fresh tomatoes , mayo and mustard.)
• Patty Melt ................................................................................7.99
• Cheese Burger ........................................................................6.99
• Double Cheese Burger............................................................7.99
• Grilled or Fried Chicken Burger ................................................6.99
• Fish Burger ..............................................................................6.99
• (breaded fish with lettuce, tomatoes & tartar sauce )
• Blt..................................................................................4.99
• (bacon , lettuce & tomato sandwich )
• *******all burgers are served with french fries ***************
• *******ADD THREE SLICES OF BACON TO ANY BURGER ******
• ..................................1.25.
• **************KIDS MENU *****************
• Hamburger combo ..................................3.50
• cheese burger combo ..............................3.99
• Grilled ham and cheese ...........................3.50
• Chicken Tenders .......................................3.99
• Enchilada plate .........................................3.99
• (two enchiladas , rice & beans )
• Ground Beef tacos ...................................3.99
• (2 crispy or soft ground beef tacos , lettuce and cheese )
• ***************SPECIALTIES ***********************
• Chile Relleno ......................................................9.99
• (ground beef or cheese )
• Shrimp and cheese Chile Relleno ......................10.99
• Hamburger steak .................................................8.99
• 8 oz Grilled Chicken Breast .................................8.99
• Chicken Fried Chicken ........................................8.99
• Chicken Fried Steak .............................................8.99
• T Bone .................................................................12.99
• Pork Chops ..........................................................8.99
• Arrachera Steak ...................................................9.99
• ****************COMBINATION PLATES***********************
• Kandry's Special ..................................................8.99
• (fajita with two enchiladas on the side , rice and beans )
• Tampiquena .........................................................9.99
• (fajita steak with two enchiladas on the side , rice and beans
• Rio Bravo Plate .....................................................11.99
• (1 beef or cheese chile relleno with fajita steak on the side , rice and beans )
• Fajita & Shrimp plate .............................................11.99
• T Bone & Shrimp ......................................................13.99
• ************SOUTH OF THE BORDER ****************
• Cheese Enchiladaas ..................................................7.99
• Beef or Chicken Enchiladas ......................................8.99
• Mexican Plate .............................................................9.50
• (three enchiladas , one ground beef taco, and one chicken chalupa )
• Bean and Cheese Chalupa...........................................7.99
• Beef or Chicken Chalupas............................................8.99
• Chicken Flautas ..........................................................8.99
• Beef Milanesa .............................................................8.99
• Chicken Milanesa..........................................................8.99
• Bisteck Ranchero ..........................................................8.99
• Fajita or Chicken plate ...................................................8.99
• Fajita Toreada ................................................................8.99
• Pechuga Santa Fe.........................................................8.99
• Carne Guisada Plate......................................................8.99
• Fajita or Chicken Quesadillas .......................................9.99
• Shrimp Quesadillas ......................................................10.99
• Fajita or Chicken Tacos .................................................8.99
• Ground Beef tacos ( crispy or soft )...............................7.99
• **all Plates are served with rice and beans ***
• ****************TACOS ************
• Chicken fajita taco .....................................2.99
• Fajita taco ..................................................2.99
• Carne guisada ..........................................2.99
• Ground Beef taco ......................................2.50
• ************SOUPS ******************
• Caldo de Res ..........................small 6.99.................large....7.99
• Caldo de Pescado y Camaron ..small 7.99..............large ....8.99
• Caldo Siete Mares .....................small 8.99.............large ....9.99
• Menudo ....................................small ..6.99.............large ..7.99
• Caldo Tlalpeno ..........................small .. 7.99........large 8.99
• *********SEAFOOD*************
• Fish Tacos .................................................8.99
• (fish filet on corn tortilla , rice on the side )
• Fish Plate (Grilled or Fried ).........................11.99
• Shrimp Plate (any style)................................12.99
• (al mojo de ajo, ala diabla, agua chiles , fried)
• Costa Azul ....................................................14.99
• ( 6 shrimp wrapped in bacon and breaded to perfection , filled with mozzarella cheese , served with fries , rice and salad )
• Seafood Fiesta .............................................14.99
• ( combination of fish , shrimp and crab)
• Shrimp Cocktail .......................................small ..9.99.....large...12.99
• ***********FAMILY PLATTERS **************************
• Botana or Sombrero for 1 .............................................10.99
• Botana or Sombrero for 2 ..............................................20.99
• Botana or Sombrero for 3 ..............................................27.99
• Botana or Sombrero for 4 ..............................................38.99
• Botana or Sombrero for 6................................................49.99
• (beef chicken or mixed )
• Seafood platter for 2 ........................................................25.99
• Seafood platter for 3 ........................................................33.99
• Seafood platter for 4 ........................................................44.99
• Seafood platter for 6.........................................................59.99
• Mar y Tierra for 2 ............................................................26.99
• Mar y Tierra for 3 ............................................................35.99
• Mar y Tierra for 4 .............................................................43.99
• Mar y Tierra for 6...............................................................58.99
• *********BREAKFAST PLATES *************************
• Potato & Egg Plate ...................................4.99
• Bacon & Egg Plate ....................................4.99
• Migas & Egg Plate.....................................4.99
• Huevos Rancheros ...................................4.99
• Huevo ala Mexicana ..................................4.99
• Chorizo & Egg Plate ..................................4.99
• Sausage & Egg Plate ................................4.99
• Ham & Egg Plate........................................4.99
• Machacado & Egg Plate ............................5.99
• Chicharron en Salsa.....................................5.99
• Chicharron & Egg Plate................................5.99
• Chicharron en salsa with 2 eggs ..................6.99
• Chilaquiles .................................................5.99
• Huevos Divorciados ...................................6.99
• Chicken Chilaquiles ..................................6.99
• Fajita Asada & egg ......................................7.99
• Barbacoa Plate ............................................6.99
• ( add two eggs )............................................7.99
• **************GOURMET BREAKFAST*****
• Kandry's Favorite .............................................7.99
• two eggs , one slice of ham , two bacon , two sausage links and two buttermilk pancakes
• Kandry's Special ..........................................................3.99
• Two eggs , sausage , ham or bacon
• Ham and cheese Omelette .......................................6.99
• three egg omelette filled with ham and cheese , hash-brown and toast.
• Ultimate Omelette ....................................................7.99
• Three egg omelette with sausage , bacon , fire roasted bell peppers and onion , mushrooms , diced tomatoes and shredded cheese . served with hash-browns and toast .
• Meat lovers Omelette ......................................................8.99
• Three egg omelette with grilled steak , fire roasted bell peppers and onions.
• sauteed mushrooms and melted mozzarella cheese.
• The steakwich ...............................................7.99
• two scrambled eggs, tender steak , american cheese on texas toast .
• Hamwich .......................................................5.99
• sausagewich .................................................5.99
• Chicken Fried steak and eggs .......................7.99
• Pork chops and Eggs .....................................9.99
• T Bone Steak and eggs ...............................10.99
• **********BREAKFAST TACOS ********************
• Bacon & egg ...................1.99
• Sausage & Egg ................1.99
• Potato & Egg...................1.99
• Chorizo & Egg .................1.99
• Bean &Egg.......................1.99
• Ham and Egg ....................1.99
• Machacado & Egg ............2.59
• Chicharron & Egg .............2.59
• Gorditas .............................2.99
• *****extra taco filling *** .35
• *********DRINKS ***********
• Coffee..............................1.99
• Milk ..................................1.99
• Orange Juice ...................2.50
• (no refill )
• Sweet & unsweet Tea ..........2.15
• Raspberry Tea ...................2.50
• Fountain Drinks ..................2.15
• Strawberry lemonade ...........2.50
• Lemonade .............................2.50
• hot chocolate ...........................1.99
• *****15% WILL BE ADDED ON TABLES OF 6 OR MORE ***

```html
<!DOCTYPE html>
<html lang="en">
<head>
<meta charset="utf-8">
<title>Kandry's Menu</title>
<link href="https://fonts.googleapis.com/css2?family=Delius&display=swap" rel="stylesheet">
<style>
:root{
  --red:#b8141c;
  --red-deep:#8e0c12;
  --gold:#f6b51e;
  --gold-light:#f9c440;
  --green:#1d8a2c;
  --cream:#fff6d8;
  --note-warm:#f0a83a;
  --ink-red:#b4101a;
  --note-red:#e0481b;
  --white:#ffffff;
}
*{margin:0;padding:0;box-sizing:border-box}
html,body{width:1200px;height:776px;overflow:hidden;background:#fff}
body{font-family:"Delius",cursive;font-size:10.6px}
.menu{position:relative;width:1200px;height:776px;display:flex}
.panel{position:relative;width:400px;height:776px;overflow:hidden}
.panel--red{background:radial-gradient(ellipse at 50% 45%,var(--red) 55%,var(--red-deep) 100%);color:var(--cream)}
.panel--gold{background:repeating-linear-gradient(90deg,var(--gold) 0 5px,var(--gold-light) 5px 9px);color:var(--ink-red)}
.banner{position:absolute;height:33px;background:var(--green);border-radius:50%;color:var(--white);
  display:flex;align-items:center;justify-content:center;font-size:15px;letter-spacing:.3px;
  box-shadow:0 0 0 1px rgba(0,0,0,.05)}
.photo{position:absolute;border-radius:50%;border:2px dashed var(--green);padding:3px}
.photo span{display:block;width:100%;height:100%;border-radius:50%}
.block{position:absolute}
.row{display:flex;align-items:baseline;white-space:nowrap}
.dots{flex:1;border-bottom:1px dotted currentColor;margin:0 2px;min-width:4px;transform:translateY(-2px);opacity:.8}
.desc{color:var(--note-warm);line-height:15px}
.panel--gold .desc{color:var(--note-red)}
.note{position:absolute;white-space:nowrap;color:var(--white)}
.panel--gold .note{color:var(--ink-red)}
.r17{line-height:16.7px}
.r15{line-height:15.3px}
.r14{line-height:14.6px}
.cols{display:flex;gap:18px}
.cols>div{flex:1}
.head-small{position:absolute;color:var(--white);font-size:10.6px}
</style>
</head>
<body>
<main class="menu">

  <!-- Left panel -->
  <section class="panel panel--red">
    <div class="banner" style="left:57px;top:21px;width:193px">APPETIZERS</div>
    <div class="block r17" style="left:28px;top:61px;width:340px">
      <div class="row"><span>Jalapeno cheese fries</span><span class="dots"></span><span>4.99</span></div>
      <div class="row"><span>Mozzarella cheese sticks</span><span class="dots"></span><span>5.25</span></div>
      <div class="row"><span>Classic Nachos ( ground bee)</span><span class="dots"></span><span>6.99</span></div>
      <div class="row"><span>Nachos ( fajita or chicken fajita )</span><span class="dots"></span><span>7.99</span></div>
      <div class="row"><span>Panchos ( includes lettuce , and avocado )</span><span class="dots"></span><span>8.99</span></div>
      <div class="row"><span>Shrimp Nachos</span><span class="dots"></span><span>8.99</span></div>
      <div class="row"><span>Choriqueso</span><span class="dots"></span><span>6.99</span></div>
      <div class="row"><span>Guacamole</span><span class="dots"></span><span>5.99</span></div>
    </div>

    <div class="banner" style="left:57px;top:218px;width:193px">SALADS</div>
    <div class="photo" style="left:10px;top:252px;width:94px;height:94px">
      <span role="img" aria-label="Photo of a grilled steak plate with peppers and fries" style="background:radial-gradient(circle at 55% 50%,#6a3a1c,#a9432a 45%,#3f6a2a 80%,#d9c8a0)"></span>
    </div>
    <div class="block r17" style="left:120px;top:260px;width:248px">
      <div class="row" style="margin-left:5px"><span>House Salad</span><span class="dots"></span><span>5.99</span></div>
      <div class="row" style="margin-left:10px"><span>Caesar Salad</span><span class="dots"></span><span>5.99</span></div>
      <div class="row" style="margin-left:17px"><span>Chef Salad</span><span class="dots"></span><span>7.99</span></div>
      <div class="row" style="margin-left:15px"><span>Grilled or Crispy chicken Salad</span><span class="dots"></span><span>8.99</span></div>
      <div class="row" style="margin-left:7px"><span>Shrimp Salad</span><span class="dots"></span><span>9.99</span></div>
    </div>

    <div class="banner" style="left:57px;top:359px;width:288px">BURGERS AND SANDWICHES</div>
    <div class="block r15" style="left:28px;top:400px;width:340px">
      <div class="row"><span>Fajita Steak Burger</span><span class="dots"></span><span>8.95</span></div>
      <div class="desc">Fine cut fajita loaded with fresh sauteed mushrooms , and topped with mozzarella cheese, crisp lettuce , onions , tomatoes mayo &amp; mustard</div>
      <div class="row"><span>Mushroom Swiss Burger</span><span class="dots"></span><span>8.95</span></div>
      <div class="desc">Loaded with fresh saureed mushrooms, and topped with melted Swiss cheese</div>
      <div class="row"><span>Hawaiian Burger</span><span class="dots"></span><span>7.99</span></div>
      <div class="desc">Topped with pineapple , american cheese , crisp lettuce , tomatoes and mayo</div>
      <div class="row"><span>Barbecue Burger</span><span class="dots"></span><span>7.99</span></div>
      <div class="desc">Basted with our original Bbq sauce, American cheese , lettuce , fresh tomatoes , mayo and mustard</div>
      <div class="row"><span>Patty Melt</span><span class="dots"></span><span>7.99</span></div>
      <div class="row"><span>Cheese Burger</span><span class="dots"></span><span>6.99</span></div>
      <div class="row"><span>Double Cheese Burger</span><span class="dots"></span><span>7.99</span></div>
      <div class="row"><span>Grilled or Fried Chicken Burger</span><span class="dots"></span><span>6.99</span></div>
      <div class="row"><span>Fish Burger</span><span class="dots"></span><span>6.99</span></div>
      <div class="desc">Breaded fish with lettuce, tomatoes &amp; tartar sauce</div>
      <div class="row"><span>Blt</span><span class="dots"></span><span>4.99</span></div>
      <div class="desc">Bacon, lettuce &amp; tomato sandwich</div>
    </div>
    <div class="note" style="left:152px;top:726px">* Add 3 slices of Bacon to any burger 1.25</div>
    <div class="note" style="left:76px;top:751px">*** all burgers are served with french fries ***</div>
  </section>

  <!-- Middle panel -->
  <section class="panel panel--gold">
    <div class="banner" style="left:61px;top:21px;width:279px">SPECIALTIES</div>
    <div class="photo" style="left:8px;top:47px;width:121px;height:121px">
      <span role="img" aria-label="Photo of a chile relleno plate with rice, beans and guacamole" style="background:radial-gradient(circle at 45% 55%,#c98a3a,#7a3d1a 45%,#5d8f3a 75%,#efe6cf)"></span>
    </div>
    <div class="block r17" style="left:116px;top:61px;width:255px">
      <div class="row" style="margin-left:8px"><span>Chile Relleno</span><span class="dots"></span><span>9.99</span></div>
      <div class="desc" style="margin-left:22px">Ground beef or cheese</div>
      <div class="row" style="margin-left:25px"><span>Shrimp and cheese Chile Relleno</span><span class="dots"></span><span>10.99</span></div>
      <div class="row" style="margin-left:28px"><span>Hamburger steak</span><span class="dots"></span><span>8.99</span></div>
      <div class="row" style="margin-left:28px"><span>8 oz Grilled Chicken Bread</span><span class="dots"></span><span>8.99</span></div>
      <div class="row" style="margin-left:23px"><span>Chicken Fried Chicken</span><span class="dots"></span><span>8.99</span></div>
      <div class="row" style="margin-left:13px"><span>Chicken Fried Steak</span><span class="dots"></span><span>8.99</span></div>
      <div class="row" style="margin-left:0"><span>T Bone</span><span class="dots"></span><span>12.99</span></div>
    </div>
    <div class="block r17" style="left:29px;top:195px;width:342px">
      <div class="row"><span>Pork Chops</span><span class="dots"></span><span>8.99</span></div>
      <div class="row"><span>Arrachera Steak</span><span class="dots"></span><span>9.99</span></div>
    </div>

    <div class="banner" style="left:61px;top:241px;width:279px">COMBINATION PLATES</div>
    <div class="block r15" style="left:29px;top:281px;width:342px">
      <div class="row"><span>Kandry's Special</span><span class="dots"></span><span>8.99</span></div>
      <div class="desc">Fajita with two enchiladas on the side , rice and beans</div>
      <div class="row"><span>Tampiquena</span><span class="dots"></span><span>9.99</span></div>
      <div class="desc">Fajita steak with two enchiladas on the side , rice and beans</div>
      <div class="row"><span>Rio Bravo Plate</span><span class="dots"></span><span>11.99</span></div>
      <div class="desc">1 beef or cheese chile relleno with fajita steak on the side , rice and beans</div>
      <div class="row"><span>Fajita &amp; Shrimp plate</span><span class="dots"></span><span>11.99</span></div>
      <div class="row"><span>T Bone &amp; Shrimp</span><span class="dots"></span><span>13.99</span></div>
    </div>

    <div class="banner" style="left:61px;top:435px;width:260px">FROM THE BAR-B-QUE</div>
    <div class="block r15" style="left:29px;top:474px;width:226px">
      <div>Baby Back Ribs</div>
      <div class="row desc"><span>Half rack</span><span class="dots"></span><span>12.99</span></div>
      <div class="row desc"><span>Full rack</span><span class="dots"></span><span>18.99</span></div>
      <div class="row"><span>Brisket Burger</span><span class="dots"></span><span>8.25</span></div>
      <div class="row"><span>Barbecue Combo</span><span class="dots"></span><span>17.99</span></div>
      <div class="desc">Half rack of ribs, brisket, and sausage</div>
      <div class="desc">Served with potato salad and red beans</div>
    </div>
    <div class="photo" style="left:266px;top:495px;width:122px;height:122px">
      <span role="img" aria-label="Photo of a barbecue plate with brisket, rice and tortilla chips" style="background:radial-gradient(circle at 50% 50%,#3d2414,#8a5a2a 40%,#d9b66a 70%,#5e8a3a)"></span>
    </div>

    <div class="banner" style="left:61px;top:592px;width:279px">FAMILY PLATTERS</div>
    <div class="block r17" style="left:29px;top:633px;width:176px">
      <div class="row"><span>Botana or Sombrero for 1</span><span class="dots"></span><span>10.99</span></div>
      <div class="row"><span>Botana or Sombrero for 2</span><span class="dots"></span><span>20.99</span></div>
      <div class="row"><span>Botana or Sombrero for 3</span><span class="dots"></span><span>27.99</span></div>
      <div class="row"><span>Botana or Sombrero for 4</span><span class="dots"></span><span>38.99</span></div>
      <div class="row"><span>Botana or Sombrero for 6</span><span class="dots"></span><span>49.99</span></div>
      <div class="desc" style="line-height:16.7px">Beef chicken or mixed</div>
      <div class="row"><span>Seafood platter for 2</span><span class="dots"></span><span>25.99</span></div>
      <div class="row"><span>Seafood platter for 3</span><span class="dots"></span><span>33.99</span></div>
    </div>
    <div class="block r17" style="left:223px;top:633px;width:148px">
      <div class="row"><span>Seafood platter for 4</span><span class="dots"></span><span>44.99</span></div>
      <div class="row"><span>Seafood patter for 6</span><span class="dots"></span><span>59.99</span></div>
      <div class="row"><span>Mar y Tierra for 2</span><span class="dots"></span><span>26.99</span></div>
      <div class="row"><span>Mar y Tierra for 3</span><span class="dots"></span><span>35.99</span></div>
      <div class="row"><span>Mar y Tierra for 4</span><span class="dots"></span><span>43.99</span></div>
      <div class="row"><span>Mar y Tierra for 6</span><span class="dots"></span><span>58.99</span></div>
    </div>
  </section>

  <!-- Right panel -->
  <section class="panel panel--red">
    <div class="banner" style="left:58px;top:21px;width:283px">KIDS MENU</div>
    <div class="block r17" style="left:29px;top:61px;width:162px">
      <div class="row"><span>Hamburger combo</span><span class="dots"></span><span>3.50</span></div>
      <div class="row"><span>Cheese burger combo</span><span class="dots"></span><span>3.99</span></div>
      <div class="row"><span>Grilled ham and cheese</span><span class="dots"></span><span>3.50</span></div>
      <div class="row"><span>Chicken Tenders</span><span class="dots"></span><span>3.99</span></div>
    </div>
    <div class="block" style="left:209px;top:61px;width:163px;line-height:14px">
      <div class="row" style="line-height:16.7px"><span>Enchilada plate</span><span class="dots"></span><span>3.99</span></div>
      <div class="desc" style="line-height:14px">Two enchiladas , rice &amp; beans</div>
      <div class="row" style="line-height:18px"><span>Ground Beef tacos</span><span class="dots"></span><span>3.99</span></div>
      <div class="desc" style="line-height:14px">Two crispy or soft ground beef tacos , lettuce and cheese</div>
    </div>

    <div class="banner" style="left:58px;top:147px;width:288px">PASTAS</div>
    <div class="block r17" style="left:31px;top:188px;width:252px">
      <div class="row"><span>Chicken Fettuccine or Penne Pasta</span><span class="dots"></span><span>9.25</span></div>
      <div class="row"><span>Shrimp Fettuccine or Penne Pasta</span><span class="dots"></span><span>10.25</span></div>
    </div>
    <div class="photo" style="left:293px;top:188px;width:105px;height:105px">
      <span role="img" aria-label="Photo of glazed chicken wings" style="background:radial-gradient(circle at 45% 50%,#7a1a08,#c0461a 50%,#e07a30 80%,#f3e6d0)"></span>
    </div>

    <div class="banner" style="left:58px;top:235px;width:257px">WINGS</div>
    <div class="block r17" style="left:31px;top:274px;width:155px">
      <div>Boneless or Traditional</div>
      <div class="row"><span>5 Wings</span><span class="dots"></span><span>5.99</span></div>
      <div class="row"><span>10 Wings</span><span class="dots"></span><span>8.99</span></div>
    </div>
    <div class="block r17" style="left:210px;top:291px;width:162px">
      <div class="row"><span>20 Wings</span><span class="dots"></span><span>14.99</span></div>
      <div class="row"><span>50 Wings</span><span class="dots"></span><span>35.99</span></div>
    </div>
    <div class="block desc" style="left:31px;top:326px;white-space:nowrap">Mild , hot , lemon pepper , sweet chili , teriyaki , garlic Parmesan</div>

    <div class="banner" style="left:58px;top:353px;width:288px">SOUTH OF THE BORDER</div>
    <div class="block" style="left:31px;top:393px;width:161px;line-height:16.4px">
      <div class="row"><span>Cheese Enchiladaas</span><span class="dots"></span><span>7.99</span></div>
      <div>Beef or Chicken Enchiladas</div>
      <div class="row"><span class="dots" style="margin-left:0"></span><span>8.99</span></div>
      <div class="row"><span>Mexican Plate</span><span class="dots"></span><span>9.50</span></div>
      <div class="desc" style="line-height:14.4px">Three enchiladas , one ground beef taco, and one chicken chalupa</div>
      <div style="margin-top:3px">Bean and Cheese Chalupa</div>
      <div class="row"><span class="dots" style="margin-left:0"></span><span>7.99</span></div>
      <div>Beef or Chicken Chalupas</div>
      <div class="row"><span class="dots" style="margin-left:0"></span><span>8.99</span></div>
      <div class="row"><span>Chicken Flautas</span><span class="dots"></span><span>8.99</span></div>
      <div class="row"><span>Beef Milanesa</span><span class="dots"></span><span>8.99</span></div>
    </div>
    <div class="block" style="left:211px;top:393px;width:161px;line-height:16.8px">
      <div class="row"><span>Chicken Milanesa</span><span class="dots"></span><span>8.99</span></div>
      <div class="row"><span>Bisteck Ranchero</span><span class="dots"></span><span>8.99</span></div>
      <div class="row"><span>Fajita or Chicken plate</span><span class="dots"></span><span>8.99</span></div>
      <div class="row"><span>Fajita Toreada</span><span class="dots"></span><span>8.99</span></div>
      <div class="row"><span>Pechuga Santa Fe</span><span class="dots"></span><span>8.99</span></div>
      <div class="row"><span>Carne Guisada Plate</span><span class="dots"></span><span>8.99</span></div>
      <div>Fajita or Chicken Quesadillas</div>
      <div class="row"><span class="dots" style="margin-left:0"></span><span>9.99</span></div>
      <div class="row"><span>Shrimp Quesadillas</span><span class="dots"></span><span>10.99</span></div>
      <div class="row"><span>Fajita or Chicken Tacos</span><span class="dots"></span><span>8.99</span></div>
      <div style="line-height:14px">Ground Beef tacos ( crispy or</div>
      <div class="row" style="line-height:15px"><span>soft )</span><span class="dots"></span><span>7.99</span></div>
    </div>
    <div class="note" style="left:78px;top:600px">*** all plates are served with rice and beans ***</div>

    <div class="banner" style="left:58px;top:627px;width:288px">SOUPS</div>
    <div class="head-small" style="left:186px;top:667px">Small</div>
    <div class="head-small" style="left:229px;top:667px">Large</div>
    <div class="block r17" style="left:31px;top:682px;width:250px">
      <div class="row"><span>Caldo de Res</span><span class="dots"></span><span>6.99</span><span style="width:43px;text-align:right">7.99</span></div>
      <div class="row"><span>Caldo de Pescado y Camaron</span><span class="dots"></span><span>7.99</span><span style="width:43px;text-align:right">8.99</span></div>
      <div class="row"><span>Caldo Siete Mares</span><span class="dots"></span><span>8.99</span><span style="width:43px;text-align:right">9.99</span></div>
      <div class="row"><span>Menudo</span><span class="dots"></span><span>6.99</span><span style="width:43px;text-align:right">7.99</span></div>
      <div class="row"><span>Caldo Tlalpeno</span><span class="dots"></span><span>7.99</span><span style="width:43px;text-align:right">8.99</span></div>
    </div>
    <div class="photo" style="left:276px;top:658px;width:110px;height:110px">
      <span role="img" aria-label="Photo of a soup bowl with a side plate" style="background:radial-gradient(circle at 50% 50%,#e8d6a8,#c98e3a 45%,#6a9a3a 70%,#f2ece0)"></span>
    </div>
  </section>

</main>
</body>
</html>
```